POLITICAL CARD TO HAND OUT

A LITTLE LARGER THAN THE REGULAR BUSINESS CARD WITH THE ABOVE INFORMATION.

Industry/Entity Type

Business

Contact Information for Business Card

ELECT *DEAN HOLT* FOR JUSTICE OF THE PEACE PCT 6-EXPERIENCED LEADERSHIP- WITH MY PICTURE ON IT- PHONE 347-610-2853-MERIDIAN PRIMARY - EARLY VOTING FEB 18TH THRU FEB 28 AND ELECTION DAY IS MARCH 4TH, 2014- USE RED WHITE AND BLUE WITH SOME STARS.

Requirements
Must have
• A FIVE POINTED STAR ON EACH SIDE OF MY NAME

```html
<!DOCTYPE html>
<html lang="en">
<head>
<meta charset="utf-8">
<title>Dean Holt for Justice of the Peace</title>
<link rel="stylesheet" href="https://fonts.googleapis.com/css2?family=Alfa+Slab+One&family=Open+Sans:wght@400;600&display=swap">
<style>
  :root {
    --flag-red: #ee1c25;
    --flag-blue: #2b2fd6;
    --flag-blue-light: #4a52ec;
    --outline-blue: #1d23c8;
    --paper: #ffffff;
    --ink: #111111;
    --sky-light: #eaf6fb;
    --sky: #b9e0ef;
    --suit: #1a1414;
  }
  * { margin: 0; padding: 0; box-sizing: border-box; }
  html, body { width: 1200px; height: 702px; overflow: hidden; background: var(--paper); }
  .card { position: relative; width: 1200px; height: 702px; background: var(--paper); }

  .banner {
    position: absolute; left: 22px; top: 22px; width: 635px; height: 488px;
    background: var(--flag-red);
  }
  .banner__field {
    position: absolute; left: 23px; top: 0; width: 590px; height: 488px;
    background: radial-gradient(ellipse at 40% 45%, var(--flag-blue-light), var(--flag-blue) 70%);
  }
  .band { position: absolute; left: 0; width: 100%; background: var(--paper); }
  .band--elect { top: 48px; height: 42px; }
  .band--office { top: 218px; height: 106px; }

  .star-row { position: absolute; top: 9px; display: flex; gap: 12px; }
  .star-row--left { left: 14px; }
  .star-row--right { right: 14px; }
  .star-row svg { width: 25px; height: 25px; }

  .elect {
    position: absolute; top: 4px; left: 0; width: 100%; text-align: center;
    font-family: "Alfa Slab One", serif; font-size: 29px; color: var(--flag-red);
    letter-spacing: 1px;
  }

  .nameplate {
    position: absolute; top: 108px; left: 0; width: 100%; height: 70px;
    display: flex; align-items: center; justify-content: center; gap: 10px;
  }
  .candidate {
    font-family: "Alfa Slab One", serif; font-size: 46px; color: var(--paper);
    letter-spacing: 1px; line-height: 70px; white-space: nowrap;
  }
  .name-star {
    flex: none; width: 52px; height: 52px;
    filter: drop-shadow(0 0 8px #ffffff) drop-shadow(0 0 16px #cfd8ff);
  }

  .office {
    position: absolute; top: 12px; left: 0; width: 100%; text-align: center;
    font-family: "Alfa Slab One", serif; font-size: 26px; line-height: 44px;
    color: var(--flag-red); letter-spacing: 1px;
  }
  .contact {
    position: absolute; left: 13px; top: 360px;
    font-family: "Open Sans", sans-serif; font-size: 34px; line-height: 48px;
    color: var(--paper);
  }

  .dates { position: absolute; left: 25px; top: 513px; width: 630px; }
  .dates__row {
    border: 3px solid var(--flag-red); background: var(--paper);
    font-family: "Open Sans", sans-serif; font-size: 31px; color: var(--ink);
    padding-left: 9px; height: 48px; line-height: 42px; margin-bottom: 6px;
    white-space: nowrap; overflow: hidden;
  }
  .dates__row--last { height: 56px; line-height: 50px; padding-left: 4px; }

  .portrait {
    position: absolute; left: 660px; top: 22px; width: 518px; height: 655px;
    background:
      linear-gradient(to bottom, transparent 50%, var(--suit) 52%),
      radial-gradient(ellipse at 50% 40%, var(--sky-light), var(--sky) 75%);
  }
</style>
</head>
<body>
<svg width="0" height="0" style="position:absolute">
  <symbol id="star" viewBox="-50 -52 100 100">
    <polygon points="0,-50 11.2,-15.5 47.6,-15.5 18.2,5.9 29.4,40.5 0,19.1 -29.4,40.5 -18.2,5.9 -47.6,-15.5 -11.2,-15.5"/>
  </symbol>
</svg>

<main class="card">
  <section class="banner">
    <div class="banner__field" role="img" aria-label="Blue field scattered with lighter blue stars">
      <div class="band band--elect">
        <div class="star-row star-row--left">
          <svg fill="none" stroke="var(--outline-blue)" stroke-width="7"><use href="#star"/></svg>
          <svg fill="none" stroke="var(--outline-blue)" stroke-width="7"><use href="#star"/></svg>
          <svg fill="none" stroke="var(--outline-blue)" stroke-width="7"><use href="#star"/></svg>
          <svg fill="none" stroke="var(--outline-blue)" stroke-width="7"><use href="#star"/></svg>
          <svg fill="none" stroke="var(--outline-blue)" stroke-width="7"><use href="#star"/></svg>
        </div>
        <p class="elect">ELECT</p>
        <div class="star-row star-row--right">
          <svg fill="none" stroke="var(--outline-blue)" stroke-width="7"><use href="#star"/></svg>
          <svg fill="none" stroke="var(--outline-blue)" stroke-width="7"><use href="#star"/></svg>
          <svg fill="none" stroke="var(--outline-blue)" stroke-width="7"><use href="#star"/></svg>
          <svg fill="none" stroke="var(--outline-blue)" stroke-width="7"><use href="#star"/></svg>
          <svg fill="none" stroke="var(--outline-blue)" stroke-width="7"><use href="#star"/></svg>
        </div>
      </div>

      <div class="nameplate">
        <svg class="name-star" fill="#ffffff"><use href="#star"/></svg>
        <h1 class="candidate">DEAN HOLT</h1>
        <svg class="name-star" fill="#ffffff"><use href="#star"/></svg>
      </div>

      <div class="band band--office">
        <p class="office">FOR JUSTICE OF THE PEACE<br>PCT 6-EXPERIENCED LEADERSHIP</p>
      </div>

      <p class="contact">PHONE 347-610-2853<br>MERIDIAN PRIMARY</p>
    </div>
  </section>

  <section class="dates">
    <p class="dates__row">EARLY VOTING</p>
    <p class="dates__row">FEB 18TH THRU FEB 28</p>
    <p class="dates__row dates__row--last">ELECTION DAY IS MARCH 4TH&nbsp; 2014</p>
  </section>

  <div class="portrait" role="img" aria-label="Photo of the candidate in a white cowboy hat and dark suit against a pale blue backdrop"></div>
</main>
</body>
</html>
```